Pemberton Dialworks Business Card Design

Double Sided Business Card Design for a Locksmith company specializing in Safecracking, safe & vault service.

```html
<!DOCTYPE html>
<html lang="en">
<head>
<meta charset="utf-8">
<title>Pemberton Dialworks Business Card</title>
<link href="https://fonts.googleapis.com/css2?family=Poppins:wght@400;500;600;800&display=swap" rel="stylesheet">
<style>
  :root {
    --green: #2a8a42;
    --green-dark: #1e7434;
    --ink: #1c1c1c;
    --text: #2b2b2b;
    --paper: #ffffff;
    --stage: #e9ebe8;
  }
  * { margin: 0; padding: 0; box-sizing: border-box; }
  html, body { width: 1200px; height: 912px; overflow: hidden; }
  body {
    background: var(--stage);
    font-family: "Poppins", sans-serif;
    position: relative;
  }
  .card {
    position: absolute;
    width: 540px;
    height: 310px;
    border-radius: 22px;
    overflow: hidden;
    box-shadow: 0 10px 28px rgba(0,0,0,0.18);
  }
  /* Front */
  .card-front {
    left: 60px; top: 120px;
    background: linear-gradient(135deg, var(--green) 0%, var(--green-dark) 100%);
  }
  .card-front .brand {
    position: absolute;
    left: 60px; top: 118px;
    display: flex; align-items: center; gap: 16px;
  }
  .brand-dot {
    width: 64px; height: 64px; border-radius: 50%;
    background: var(--paper);
    flex: none;
  }
  .brand-name {
    font-weight: 800;
    font-size: 30px;
    line-height: 1.02;
    letter-spacing: 0.5px;
    text-transform: uppercase;
    color: var(--paper);
  }
  /* Back */
  .card-back {
    left: 600px; top: 470px;
    background: var(--paper);
  }
  .card-back .brand {
    position: absolute;
    left: 36px; top: 126px;
    display: flex; align-items: center; gap: 12px;
  }
  .card-back .brand-dot { width: 50px; height: 50px; background: var(--green); }
  .card-back .brand-name { font-size: 22px; color: var(--green); }
  .divider {
    position: absolute;
    left: 290px; top: 52px;
    width: 2px; height: 150px;
    background: var(--green);
  }
  .contact {
    position: absolute;
    left: 312px; top: 44px;
    color: var(--text);
    font-size: 13px;
    line-height: 1.35;
  }
  .contact .person {
    font-weight: 600;
    font-size: 19px;
    color: var(--green);
    letter-spacing: 0.5px;
    text-transform: uppercase;
  }
  .contact .role { font-size: 14px; margin-bottom: 8px; }
  .contact .address { margin-bottom: 8px; }
  .contact .line { display: flex; align-items: center; gap: 6px; }
  .contact svg { width: 11px; height: 11px; flex: none; }
  .swoosh { position: absolute; left: 0; top: 0; width: 540px; height: 310px; }
</style>
</head>
<body>

  <section class="card card-front" aria-label="Card front">
    <div class="brand">
      <span class="brand-dot"></span>
      <span class="brand-name">Pemberton<br>Dialworks</span>
    </div>
  </section>

  <section class="card card-back" aria-label="Card back">
    <svg class="swoosh" viewBox="0 0 540 310" aria-hidden="true">
      <path d="M230 310 C340 285 440 245 540 232 L540 310 Z" fill="var(--green)"/>
      <path d="M200 310 C310 272 420 226 528 220 C430 238 330 282 250 310 Z" fill="var(--ink)"/>
    </svg>

    <div class="brand">
      <span class="brand-dot"></span>
      <span class="brand-name">Pemberton<br>Dialworks</span>
    </div>

    <div class="divider"></div>

    <div class="contact">
      <div class="person">Daniel Harper</div>
      <div class="role">Founder</div>
      <div class="address">418 Larkspur Avenue<br>Greenfield, OR 97401</div>
      <div class="line">
        <svg viewBox="0 0 24 24"><path fill="var(--green)" d="M6.6 10.8a15 15 0 0 0 6.6 6.6l2.2-2.2a1 1 0 0 1 1-.25 11.4 11.4 0 0 0 3.6.6 1 1 0 0 1 1 1V20a1 1 0 0 1-1 1A17 17 0 0 1 3 4a1 1 0 0 1 1-1h3.5a1 1 0 0 1 1 1c0 1.25.2 2.45.6 3.6a1 1 0 0 1-.25 1z"/></svg>
        555 014 2287
      </div>
      <div class="line">
        <svg viewBox="0 0 24 24"><rect x="2" y="5" width="20" height="14" rx="1" fill="none" stroke="var(--green)" stroke-width="2.2"/><path d="M2 6l10 7 10-7" fill="none" stroke="var(--green)" stroke-width="2.2"/></svg>
        info@pembertondial.com
      </div>
      <div class="line">
        <svg viewBox="0 0 24 24"><circle cx="12" cy="12" r="10" fill="none" stroke="var(--green)" stroke-width="2.2"/><path d="M2 12h20M12 2c3 3 3 17 0 20M12 2c-3 3-3 17 0 20" fill="none" stroke="var(--green)" stroke-width="1.8"/></svg>
        www.pembertondial.com
      </div>
    </div>
  </section>

</body>
</html>
```